Velora Aesthetica

Medical doctor providing aesthetic medicine

* Double sided card
* Logo to be on card
Other details:
* Dr. Mirela Kostvan, MSc, MD, FCFP
* #214-215, 27903 83 Ave, Marbrook, ON, L4R 2P9
* 604-718-2943
* info@veloraclinic.ca
* www.veloraclinic.ca

Industry/Entity Type

Medical / Health & Beauty

Contact Information for Business Card

see 'Project Description'

Colors
0054AA
0677BA
7BADD7
CADEEF
E8F1F8
FFF300
FFF600
FEFA6F
FFFEC7
FFFEE8

Requirements
Must have
• Modern, high-end design

```html
<!DOCTYPE html>
<html lang="en">
<head>
<meta charset="utf-8">
<title>Velora Aesthetica – Business Card</title>
<link rel="stylesheet" href="https://fonts.googleapis.com/css2?family=Montserrat:wght@400;500;600&display=swap">
<style>
  :root {
    --stage: #1f1f1f;
    --card-dark: #161616;
    --card-light: #ffffff;
    --gold: #d4aa2c;
    --ink: #111111;
    --grey: #5f5f5f;
    --emboss: #3a3a3a;
  }
  * { margin: 0; padding: 0; box-sizing: border-box; }
  html, body {
    width: 1200px; height: 901px; overflow: hidden;
    background: var(--stage);
    font-family: "Montserrat", sans-serif;
  }
  .stage {
    width: 1200px; height: 901px;
    display: flex; flex-direction: column; align-items: center; justify-content: center;
    gap: 40px;
  }
  .card {
    width: 700px; height: 400px;
    position: relative;
    box-shadow: 0 10px 30px rgba(0,0,0,.45);
  }
  .card--front { background: var(--card-dark); display: flex; align-items: center; justify-content: center; }
  .card--back { background: var(--card-light); }

  .brand { display: flex; align-items: center; gap: 14px; }
  .brand__dot { border-radius: 50%; flex: none; }
  .brand__name {
    font-weight: 500; text-transform: uppercase; white-space: nowrap;
  }
  .card--front .brand__dot { background: var(--emboss); width: 22px; height: 22px; }
  .card--front .brand__name { color: var(--emboss); font-size: 34px; letter-spacing: .22em; }

  .card--back .brand { position: absolute; left: 44px; top: 220px; }
  .card--back .brand__dot { background: var(--gold); width: 16px; height: 16px; }
  .card--back .brand__name { color: var(--gold); font-size: 19px; letter-spacing: .18em; }

  .contact { position: absolute; left: 410px; top: 70px; }
  .contact__name { font-size: 24px; font-weight: 600; color: var(--ink); }
  .contact__creds { font-size: 16px; font-weight: 500; color: var(--gold); margin-top: 2px; }
  .contact__address { font-size: 16px; color: var(--grey); line-height: 1.35; margin-top: 20px; }
  .contact__list { list-style: none; margin-top: 20px; }
  .contact__item { display: flex; align-items: center; gap: 10px; font-size: 16px; color: var(--grey); line-height: 1.5; }
  .contact__icon { width: 16px; height: 16px; flex: none; }
</style>
</head>
<body>
<main class="stage">
  <section class="card card--front" aria-label="Card front">
    <div class="brand">
      <span class="brand__dot"></span>
      <span class="brand__name">Velora Aesthetica</span>
    </div>
  </section>

  <section class="card card--back" aria-label="Card back">
    <div class="brand">
      <span class="brand__dot"></span>
      <span class="brand__name">Velora Aesthetica</span>
    </div>

    <div class="contact">
      <h1 class="contact__name">Dr. Mirela Kostvan</h1>
      <p class="contact__creds">MSc, MD, FCFP</p>
      <p class="contact__address">#214-215, 27903 83 Ave<br>Marbrook, ON, L4R 2P9</p>
      <ul class="contact__list">
        <li class="contact__item">
          <svg class="contact__icon" viewBox="0 0 16 16" aria-hidden="true"><path fill="var(--gold)" d="M3.6 1.2l2.2 2.6-1.3 1.6c.9 2 2.3 3.4 4.3 4.3l1.6-1.3 2.6 2.2-1.2 2.2C7.3 12.6 3.4 8.7 1.4 2.4z"/></svg>
          604-718-2943
        </li>
        <li class="contact__item">
          <svg class="contact__icon" viewBox="0 0 16 16" aria-hidden="true"><rect x="1" y="3.5" width="14" height="9" fill="var(--gold)"/><path d="M1.5 4l6.5 5 6.5-5" fill="none" stroke="#fff" stroke-width="1.2"/></svg>
          info@veloraclinic.ca
        </li>
        <li class="contact__item">
          <svg class="contact__icon" viewBox="0 0 16 16" aria-hidden="true"><g fill="none" stroke="var(--gold)" stroke-width="1.2"><circle cx="8" cy="8" r="6.5"/><ellipse cx="8" cy="8" rx="2.8" ry="6.5"/><path d="M1.5 8h13M2.6 4.6h10.8M2.6 11.4h10.8"/></g></svg>
          www.veloraclinic.ca
        </li>
      </ul>
    </div>
  </section>
</main>
</body>
</html>
```